Stationery Design Project

We need letterhead and business cards designed for our consulting firm. Color scheme, mostly deep blue (see logo). We are a commercial consulting work out firm, nationwide (large loans, $10MM and up). Visit our website for more info.
Updates

Project Deadline Extended
Reason: Meeting tomorrow morning to make final final decision. Would like this project to stay open to be able to provide feed back and receive final edits and approve. Thank you!!!

Target Market(s)

High end investors

Industry/Entity Type

Business

Requirements
Must have
• Letterhead must have the logo and the address

4817 Larkmoor Avenue, Suite 210, San Diego, CA 92107
Nice to have
• It would be nice to incorporate a watermark of all or some portion of the logo on the letterhead, or at least for the 2nd sheets.

Maybe our phone number: 858.555.0174
and/or webiste: www.tollandridgecap.example
Should not have
• Target users and audience of this will be men so, frilly or whimsical type designs are not preferred.

```html
<!DOCTYPE html>
<html lang="en">
<head>
<meta charset="utf-8">
<title>Tolland Ridge Capital – Business Card</title>
<link rel="stylesheet" href="https://fonts.googleapis.com/css2?family=Cinzel:wght@400;600;700&display=swap">
<style>
  :root {
    --stage: #1e2221;
    --card: #ffffff;
    --ink: #111111;
    --brand-grey: #6f6f71;
    --brand-blue: #0b7cc1;
    --band-dark: #0d4f9c;
    --band-light: #1b86cf;
    --band-text: #e8f1fa;
  }
  * { box-sizing: border-box; margin: 0; padding: 0; }
  html, body { width: 924px; height: 1200px; overflow: hidden; }
  body {
    background: var(--stage);
    font-family: "Cinzel", serif;
    position: relative;
  }
  .card {
    position: absolute;
    background: var(--card);
    border-radius: 24px;
    overflow: hidden;
  }
  .card--front { left: 85px; top: 104px; width: 768px; height: 439px; }
  .card--back  { left: 82px; top: 659px; width: 769px; height: 440px; }

  .brand {
    position: absolute;
    display: flex;
    align-items: center;
    gap: 16px;
    white-space: nowrap;
  }
  .brand__mark {
    width: 34px; height: 34px;
    background: var(--brand-blue);
    flex: none;
  }
  .brand__name {
    color: var(--brand-grey);
    font-weight: 600;
    font-size: 33px;
    letter-spacing: 1px;
  }
  .card--front .brand { left: 42px; top: 190px; }
  .card--back .brand { left: 0; right: 0; top: 178px; justify-content: center; }

  .person { position: absolute; left: 536px; top: 62px; color: var(--ink); }
  .person__name { font-size: 27px; font-weight: 700; line-height: 1.1; }
  .person__title { font-size: 19px; font-weight: 400; margin-top: 4px; letter-spacing: 1px; }

  .contact {
    position: absolute; left: 41px; top: 330px;
    font-size: 16px; color: var(--ink); white-space: nowrap;
  }
  .contact__label { font-weight: 700; }
  .contact__value { margin-right: 10px; }

  .address-band {
    position: absolute; left: 0; right: 0; bottom: 0; height: 73px;
    background: linear-gradient(90deg, var(--band-dark), var(--band-light));
    color: var(--band-text);
    font-size: 18px;
    display: flex; align-items: center;
    padding-left: 41px;
  }

  .back-web {
    position: absolute; left: 0; right: 0; top: 345px;
    text-align: center; font-size: 17px; color: var(--ink);
  }
</style>
</head>
<body>
  <section class="card card--front">
    <div class="brand">
      <span class="brand__mark"></span>
      <span class="brand__name">Tolland Ridge Capital</span>
    </div>
    <div class="person">
      <p class="person__name">Your Name</p>
      <p class="person__title">Title</p>
    </div>
    <p class="contact">
      <span class="contact__label">Phone.</span>
      <span class="contact__value">858.555.0174</span>
      <span class="contact__label">Web.</span>
      <span>www.tollandridgecap.example</span>
    </p>
    <div class="address-band">4817 Larkmoor Avenue, Suite 210, San Diego, CA 92107</div>
  </section>

  <section class="card card--back">
    <div class="brand">
      <span class="brand__mark"></span>
      <span class="brand__name">Tolland Ridge Capital</span>
    </div>
    <p class="back-web">www.tollandridgecap.example</p>
  </section>
</body>
</html>
```